Brightwell Fellowship Chapel 70th Anniversary

A poster to advertise our 70th Church Anniversary. 1951 - 2021

Brightwell Fellowship Chapel

“We will tell the next generation “ Psalm 78:4

Brightwell Fellowship Chapel, Marlow Lane, Hereford, HR4 9TX

www.brightwellchapel.org.uk

T: 01432 867201
E: office@brightwellchapel.org.uk

We give thanks for all that God has done...

Font styles to use
Serif
Sans Serif
Decorative

Requirements
Nice to have
• A modern design and text
Should not have
• Crosses or pictures of churches, doves etc...

```html
<!DOCTYPE html>
<html lang="en">
<head>
<meta charset="utf-8">
<title>Brightwell Fellowship Chapel – 70th Church Anniversary</title>
<link rel="stylesheet" href="https://fonts.googleapis.com/css2?family=Lexend:wght@700&family=Outfit:wght@300;400;700&display=swap">
<style>
  :root {
    --ink: #000000;
    --white: #ffffff;
    --pink-light: #ff8ef5;
    --magenta: #e020c8;
    --violet: #7a2ee0;
    --blue: #2b40ff;
    --cyan: #0ab4ff;
    --dot-pink: #e83fd0;
    --dot-blue: #3a3cf0;
  }
  html, body {
    margin: 0;
    padding: 0;
    width: 927px;
    height: 1200px;
    overflow: hidden;
    background: var(--ink);
  }
  .poster {
    display: block;
    width: 927px;
    height: 1200px;
  }
  .bg { fill: var(--ink); }
  .stop-pink { stop-color: var(--pink-light); }
  .stop-magenta { stop-color: var(--magenta); }
  .stop-violet { stop-color: var(--violet); }
  .stop-blue { stop-color: var(--blue); }
  .stop-cyan { stop-color: var(--cyan); }
  .dot-white { fill: var(--white); }
  .dot-pink { fill: var(--dot-pink); }
  .dot-blue { fill: var(--dot-blue); }
  .solid { fill: var(--white); }
  .outline { fill: none; stroke: var(--white); stroke-width: 3; }
  .display {
    font-family: "Lexend", "Arial Black", sans-serif;
    font-weight: 700;
    fill: var(--white);
  }
  .display-outline {
    font-family: "Lexend", "Arial Black", sans-serif;
    font-weight: 700;
    fill: none;
    stroke: var(--white);
    stroke-width: 3;
  }
  .brand-name {
    font-family: "Outfit", Arial, sans-serif;
    font-weight: 400;
    font-size: 32px;
    letter-spacing: 2px;
    fill: var(--white);
  }
  .verse {
    font-family: "Outfit", Arial, sans-serif;
    font-weight: 700;
    font-size: 74px;
    fill: var(--white);
  }
  .thanks {
    font-family: "Outfit", Arial, sans-serif;
    font-weight: 300;
    font-size: 46px;
    fill: var(--white);
  }
  .contact {
    font-family: "Outfit", Arial, sans-serif;
    font-weight: 300;
    font-size: 34px;
    fill: var(--white);
  }
  .legal {
    font-family: "Outfit", Arial, sans-serif;
    font-weight: 300;
    font-size: 23px;
    fill: var(--white);
  }
</style>
</head>
<body>
<svg class="poster" viewBox="0 0 1688 2184" xmlns="http://www.w3.org/2000/svg">
  <defs>
    <linearGradient id="band-gradient" x1="0" y1="0" x2="0.35" y2="1">
      <stop offset="0" class="stop-pink"/>
      <stop offset="0.38" class="stop-magenta"/>
      <stop offset="0.6" class="stop-violet"/>
      <stop offset="0.75" class="stop-blue"/>
      <stop offset="1" class="stop-cyan"/>
    </linearGradient>
    <linearGradient id="orb-gradient" x1="0" y1="0" x2="1" y2="1">
      <stop offset="0.15" class="stop-magenta"/>
      <stop offset="0.5" class="stop-violet"/>
      <stop offset="0.9" class="stop-cyan"/>
    </linearGradient>
  </defs>

  <!-- background -->
  <rect class="bg" x="0" y="0" width="1688" height="2184"/>
  <polygon class="band" fill="url(#band-gradient)" points="0,0 561,0 1688,1126 1688,2184 785,2184 0,1400"/>

  <!-- decorative dots -->
  <g class="dots">
    <circle class="dot-white" cx="96" cy="62" r="26"/>
    <circle class="dot-white" cx="148" cy="65" r="8"/>
    <circle class="dot-white" cx="173" cy="66" r="2"/>
    <circle cx="1168" cy="178" r="53" fill="url(#orb-gradient)"/>
    <circle class="dot-pink" cx="1007" cy="95" r="8"/>
    <circle class="dot-pink" cx="1502" cy="92" r="9"/>
    <circle class="dot-blue" cx="1125" cy="318" r="8"/>
    <circle class="dot-blue" cx="1440" cy="350" r="8"/>
    <circle class="dot-pink" cx="1606" cy="398" r="8"/>
    <circle class="dot-pink" cx="1650" cy="916" r="8"/>
    <circle class="dot-pink" cx="90" cy="1551" r="8"/>
    <circle class="dot-blue" cx="115" cy="1677" r="8"/>
    <circle class="dot-pink" cx="278" cy="1781" r="8"/>
    <circle class="dot-blue" cx="585" cy="2059" r="8"/>
  </g>

  <!-- chapel name mark -->
  <g class="brand">
    <circle class="dot-white" cx="843" cy="190" r="38"/>
    <text class="brand-name" x="843" y="282" text-anchor="middle">BRIGHTWELL FELLOWSHIP</text>
    <text class="brand-name" x="843" y="318" text-anchor="middle">CHAPEL</text>
  </g>

  <!-- 70 numeral -->
  <g class="numeral" role="img" aria-label="70">
    <path class="outline" d="M108 471 H490 Q537 471 537 518 V596 L291 1160 H165 L410 596 H108 Z"/>
    <path class="outline" fill-rule="evenodd" d="M600 683 A212 212 0 0 1 1024 683 V948 A212 212 0 0 1 600 948 Z M719 692 A93.5 93.5 0 0 1 906 692 V940 A93.5 93.5 0 0 1 719 940 Z"/>
    <path class="solid" d="M152 553 H534 Q584 553 584 603 V678 L338 1242 H208 L454 678 H152 Z"/>
    <path class="solid" fill-rule="evenodd" d="M644 765 A212 212 0 0 1 1068 765 V1030 A212 212 0 0 1 644 1030 Z M763 774 A93.5 93.5 0 0 1 950 774 V1022 A93.5 93.5 0 0 1 763 1022 Z"/>
  </g>

  <!-- TH / CHURCH -->
  <text class="display-outline" x="1058" y="733" font-size="350" textLength="427" lengthAdjust="spacingAndGlyphs">TH</text>
  <text class="display" x="1102" y="815" font-size="350" textLength="428" lengthAdjust="spacingAndGlyphs">TH</text>
  <text class="display" x="1110" y="1012" font-size="208" textLength="435" lengthAdjust="spacingAndGlyphs">CHU</text>
  <text class="display" x="1125" y="1204" font-size="208" textLength="410" lengthAdjust="spacingAndGlyphs">RCH</text>

  <text class="display" x="160" y="1464" font-size="206" textLength="1368" lengthAdjust="spacingAndGlyphs">ANNIVERSARY</text>

  <!-- verse -->
  <text class="verse" x="235" y="1592" textLength="1210" lengthAdjust="spacingAndGlyphs">“WE WILL TELL THE NEXT GENERATION “</text>
  <text class="verse" x="848" y="1662" text-anchor="middle">PSALM 78:4</text>
  <text class="thanks" x="500" y="1722" textLength="680" lengthAdjust="spacingAndGlyphs">We give thanks for all that God has done...</text>

  <!-- contact -->
  <rect class="solid" x="40" y="1847" width="66" height="5"/>
  <g class="contact-block">
    <text class="contact" x="40" y="1888">Brightwell Fellowship Chapel, Marlow Lane,</text>
    <text class="contact" x="40" y="1923">Hereford, HR4 9TX</text>
    <text class="contact" x="40" y="1958">T: 01432 867201</text>
    <text class="contact" x="40" y="1993">E: office@brightwellchapel.org.uk</text>
  </g>
  <g class="legal-block">
    <text class="legal" x="40" y="2055" textLength="479" lengthAdjust="spacing">© Brightwell Fellowship Chapel. Northgate Gospel</text>
    <text class="legal" x="40" y="2081" textLength="479" lengthAdjust="spacing">Fellowship. Registered charity 318406 (England &amp;</text>
    <text class="legal" x="40" y="2107">Wales) and SC048213 (Scotland)</text>
  </g>

  <!-- corner stripes -->
  <g class="stripes">
    <polygon class="solid" points="1407,2108 1430,2128 1407,2128"/>
    <polygon class="solid" points="1438,2108 1468,2108 1491,2128 1461,2128"/>
    <polygon class="solid" points="1498,2108 1530,2108 1553,2128 1521,2128"/>
    <polygon class="solid" points="1560,2108 1592,2108 1615,2128 1583,2128"/>
    <polygon class="solid" points="1620,2108 1642,2108 1642,2128"/>
  </g>
</svg>
</body>
</html>
```